Bref créative
Blue Maple Holdings, LLC
Business cards, stationary and envelopes, electronic stationary (Microsoft Word), email signature
Simple
Peter L. Ward
Managing Member
5180 Halvern Court, Suite A
Columbia, MO 65203
pward@bmholdco.example
Phone, email, and name will change for the additional members of the company.
We also want an electronic email signature, and electronic stationary to be used with Microsoft word.
Stationary and envelopes should tie in the theme of the business cards for a uniform look.
Also looking for a Header only version of the stationary, as well as a full page version (header and footer used for design).
Logo used in a creative way.
Horizontal Black Background
Horizontal ALL Black
Horizontal White Background
Horizontal ALL White
Vertical Black Background
Vertical ALL Black
Vertical White Background
Vertical ALL White

```html
<!DOCTYPE html>
<html lang="en">
<head>
<meta charset="utf-8">
<title>Blue Maple Holdings — Business Card</title>
<link rel="stylesheet" href="https://fonts.googleapis.com/css2?family=Open+Sans:wght@400;600;700&display=swap">
<style>
  :root {
    --backdrop: #e6e4e1;
    --card: #ffffff;
    --brand-red: #c8102e;
    --brand-red-dark: #8f0a1f;
    --swoosh: #3b3b3d;
    --ink: #4a4a4c;
    --rule: #c9c9c9;
  }
  html, body {
    margin: 0;
    padding: 0;
    width: 1200px;
    height: 780px;
    overflow: hidden;
    background: var(--backdrop);
    font-family: "Open Sans", Arial, sans-serif;
  }
  .canvas {
    position: relative;
    width: 1200px;
    height: 780px;
  }
  .card {
    position: absolute;
    left: 60px;
    top: 80px;
    width: 1080px;
    height: 620px;
    background: var(--card);
    border-radius: 34px;
    overflow: hidden;
    box-shadow: 0 10px 30px rgba(0,0,0,0.18);
  }
  .card-waves {
    position: absolute;
    inset: 0;
  }
  .holder {
    position: absolute;
    right: 48px;
    top: 36px;
    text-align: right;
    color: #fff;
  }
  .holder-name {
    margin: 0;
    font-size: 38px;
    font-weight: 700;
    line-height: 1.15;
  }
  .holder-role {
    margin: 4px 0 0;
    font-size: 25px;
    font-weight: 600;
  }
  .divider {
    position: absolute;
    left: 540px;
    top: 270px;
    width: 2px;
    height: 300px;
    background: var(--rule);
  }
  .brand {
    position: absolute;
    left: 90px;
    top: 380px;
    width: 420px;
    display: flex;
    flex-direction: column;
    align-items: center;
    gap: 22px;
  }
  .brand-dot {
    width: 110px;
    height: 110px;
    border-radius: 50%;
    background: var(--brand-red);
  }
  .brand-name {
    margin: 0;
    font-size: 34px;
    font-weight: 700;
    color: var(--brand-red);
    white-space: nowrap;
  }
  .address {
    position: absolute;
    left: 570px;
    top: 275px;
    margin: 0;
    font-size: 22px;
    line-height: 1.35;
    color: var(--ink);
    font-style: normal;
  }
  .contacts {
    position: absolute;
    left: 568px;
    top: 400px;
    margin: 0;
    padding: 0;
    list-style: none;
    font-size: 22px;
    color: var(--ink);
  }
  .contacts li {
    display: flex;
    align-items: center;
    gap: 12px;
    height: 34px;
  }
  .contacts svg {
    width: 22px;
    height: 22px;
    flex: none;
  }
</style>
</head>
<body>
<main class="canvas">
  <article class="card">
    <svg class="card-waves" viewBox="0 0 1080 620" preserveAspectRatio="none" aria-hidden="true">
      <path d="M0,0 H1080 V150 C860,150 620,120 430,170 C260,215 120,280 0,350 Z" fill="var(--brand-red)"/>
      <path d="M0,0 H1080 V110 C860,115 640,95 460,135 C300,170 150,230 0,300 Z" fill="var(--brand-red-dark)" opacity="0.25"/>
      <path d="M0,372 C120,300 260,232 440,196 C560,172 680,168 760,170 C640,180 500,210 380,255 C240,308 110,370 0,430 Z" fill="var(--swoosh)"/>
    </svg>

    <header class="holder">
      <h1 class="holder-name">Peter L. Ward</h1>
      <p class="holder-role">Managing Member</p>
    </header>

    <div class="brand">
      <span class="brand-dot" aria-hidden="true"></span>
      <p class="brand-name">Blue Maple Holdings</p>
    </div>

    <div class="divider" aria-hidden="true"></div>

    <address class="address">
      5180 Halvern Court,<br>
      Suite 12, Ashwell,<br>
      MO 65990
    </address>

    <ul class="contacts">
      <li>
        <svg viewBox="0 0 24 24" aria-hidden="true"><path d="M6.6 10.8a15 15 0 0 0 6.6 6.6l2.2-2.2c.3-.3.7-.4 1-.2 1.1.4 2.3.6 3.6.6.6 0 1 .4 1 1V20c0 .6-.4 1-1 1A17 17 0 0 1 3 4c0-.6.4-1 1-1h3.5c.6 0 1 .4 1 1 0 1.3.2 2.5.6 3.6.1.3 0 .7-.2 1z" fill="var(--brand-red)"/></svg>
        (555) 014-263
      </li>
      <li>
        <svg viewBox="0 0 24 24" aria-hidden="true"><rect x="7" y="2" width="10" height="20" rx="2" fill="var(--brand-red)"/><rect x="9" y="5" width="6" height="11" fill="#fff"/></svg>
        (555) 020-3185
      </li>
      <li>
        <svg viewBox="0 0 24 24" aria-hidden="true"><rect x="3" y="9" width="18" height="11" rx="2" fill="var(--brand-red)"/><rect x="7" y="3" width="10" height="7" fill="var(--swoosh)"/><rect x="7" y="14" width="10" height="2" fill="#fff"/></svg>
        (555) 030-5149
      </li>
      <li>
        <svg viewBox="0 0 24 24" aria-hidden="true"><rect x="2" y="5" width="20" height="14" rx="2" fill="var(--brand-red)"/><path d="M3 6l9 7 9-7" fill="none" stroke="#fff" stroke-width="1.8"/></svg>
        pward@bmholdco.example
      </li>
    </ul>
  </article>
</main>
</body>
</html>
```